Design a Stylish Front Page For Our Skincare Brand Website

We have developed a luxurious and stylish skincare serum, and we need to get a stylish front page designed.
You will get a detailed website mockup to follow, and a detailed description of each part of the website.
This will give you a full understanding of what the goal, the style and requirements is.
For a detailed task description please go to:
https://files.plorvane.com/sheet/d/7Kq2m-p9TrWbNvLs4YhQ8E1a0ZcXuF6J__dMtRo3kx/view?usp=sharing
For your convenience the mockup is attached here, and the rest of the content you can find at the link above.
In case of any questions please always feel free to reach out to me here, or ask me for other communication platforms if you prefer.
We are looking forward to see your winning design!
Female 35 plus
Skincare
1 page

```html
<!DOCTYPE html>
<html lang="en">
<head>
<meta charset="UTF-8">
<title>Vesterlund – Your Daily Skin Insurance</title>
<link rel="stylesheet" href="https://fonts.googleapis.com/css2?family=Playfair+Display:ital,wght@0,400;0,700;1,400;1,700&family=Montserrat:wght@400;500;600&display=swap">
<style>
  :root{
    --teal:#2f7f86;
    --teal-dark:#1f5f66;
    --teal-deep:#17474d;
    --teal-light:#5fa9ad;
    --ink:#1d2a30;
    --text:#4b5559;
    --white:#ffffff;
    --footer:#0f1620;
    --footer-text:#c9d1d6;
    --hero-a:#dfe4e4;
    --hero-b:#b7c6c8;
  }
  *{margin:0;padding:0;box-sizing:border-box}
  html,body{width:1200px;height:3616px;overflow:hidden;background:var(--white)}
  body{position:relative;font-family:"Montserrat",sans-serif;color:var(--text)}

  /* Header */
  .site-header{position:absolute;top:0;left:0;width:1200px;height:52px;background:rgba(23,71,77,.92);z-index:5}
  .brand{font-family:"Playfair Display",serif;font-weight:400;letter-spacing:5px;color:var(--white);font-size:24px;position:absolute;left:24px;top:11px}
  .main-nav{position:absolute;right:60px;top:0;display:flex;height:52px;align-items:center;gap:8px}
  .main-nav a{color:var(--white);text-decoration:none;font-size:14px;padding:10px 18px}
  .main-nav a.is-active{background:var(--white);color:var(--teal-deep);font-weight:600}

  /* Hero */
  .hero{position:absolute;top:0;left:0;width:1200px;height:680px;background:linear-gradient(100deg,var(--hero-a) 0%,#eef0ef 45%,var(--hero-b) 100%)}
  .hero-photo{position:absolute;left:560px;top:0;width:640px;height:680px;background:linear-gradient(90deg,rgba(200,175,160,0),rgba(214,188,170,.75) 40%,rgba(190,170,160,.6))}
  .hero-bottle{position:absolute;left:810px;top:250px;width:130px;height:340px;border-radius:14px 14px 10px 10px;background:linear-gradient(180deg,#2a8a90,#48b2b3 60%,#2a7e86)}
  .hero-title{position:absolute;left:255px;top:250px;font-family:"Playfair Display",serif;color:var(--ink);font-weight:400}
  .hero-title .line-1{display:block;font-style:italic;font-weight:700;font-size:80px;line-height:1}
  .hero-title .line-2{display:block;font-size:48px;margin-top:6px}
  .btn{display:inline-block;background:var(--teal);color:var(--white);font-family:"Montserrat",sans-serif;font-weight:600;font-size:17px;letter-spacing:1px;text-transform:uppercase;border-radius:4px;text-decoration:none;text-align:center}
  .hero .btn{position:absolute;left:262px;top:410px;padding:13px 28px}
  .slider-dots{position:absolute;left:268px;top:512px;display:flex;gap:14px}
  .slider-dots span{width:13px;height:13px;border-radius:50%;background:#8d9699}
  .slider-dots span:first-child{background:var(--teal-deep)}
  .hero-wave{position:absolute;left:0;top:500px;width:1200px;height:180px}

  /* Feature rows */
  .feature-photo{position:absolute;width:320px;height:320px;border-radius:50%;border:10px solid var(--teal);box-shadow:0 0 0 5px var(--white),0 0 0 7px var(--teal-light)}
  .feature-text{position:absolute;width:360px;text-align:center}
  .feature-text .kicker{font-family:"Playfair Display",serif;font-style:italic;color:var(--teal);font-size:34px;line-height:1.15}
  .feature-text .headline{font-family:"Playfair Display",serif;color:var(--ink);font-size:36px;line-height:1.2;margin-bottom:18px;font-weight:400}
  .feature-text p{font-size:12.5px;line-height:1.75}

  /* Guarantee band */
  .guarantee{position:absolute;left:0;top:1780px;width:1200px;height:840px}
  .guarantee-title{position:absolute;top:1945px;left:0;width:1200px;text-align:center;font-family:"Playfair Display",serif;font-style:italic;font-weight:400;color:var(--white);font-size:34px}
  .guarantee-copy{position:absolute;top:2010px;left:300px;width:600px;text-align:center;color:#dcebec;font-size:12px;line-height:1.75}
  .guarantee-video{position:absolute;left:400px;top:2110px;width:450px;height:285px;background:linear-gradient(135deg,#dbe7ee,#9fb8c6 55%,#6f8ea2)}
  .play-button{position:absolute;left:584px;top:2231px;width:44px;height:44px}

  /* Brand promise */
  .promise-brand{position:absolute;top:2690px;left:0;width:1200px;text-align:center;font-family:"Playfair Display",serif;font-style:italic;color:var(--teal);font-size:34px;letter-spacing:2px}
  .promise-title{position:absolute;top:2738px;left:0;width:1200px;text-align:center;font-family:"Playfair Display",serif;font-weight:700;color:var(--ink);font-size:34px}
  .promise-copy{position:absolute;top:2795px;left:380px;width:440px;text-align:center;font-size:12px;line-height:1.75}
  .promise-initial{position:absolute;left:440px;top:2870px;width:220px;height:330px;background:linear-gradient(180deg,#eef2f2,#f8f9f9)}
  .promise-bottle{position:absolute;left:525px;top:2880px;width:150px;height:330px;border-radius:18px 18px 12px 12px;background:linear-gradient(90deg,#237a82,#4fb6b7 50%,#247c84)}
  .promise .btn{position:absolute;left:515px;top:3228px;width:170px;padding:13px 0;box-shadow:0 4px 8px rgba(0,0,0,.25)}

  /* Footer */
  .site-footer{position:absolute;left:0;top:3304px;width:1200px;height:312px;background:var(--footer);color:var(--footer-text)}
  .site-footer .brand{position:absolute;left:0;top:44px;width:1200px;text-align:center;font-size:30px;letter-spacing:8px;color:var(--footer-text)}
  .footer-cols{position:absolute;top:118px;left:0;width:1200px}
  .footer-cols ul{list-style:none;position:absolute;top:0}
  .footer-cols li{font-size:12px;line-height:2.3;padding-left:18px;position:relative}
  .footer-cols li::before{content:"";position:absolute;left:0;top:12px;width:5px;height:5px;border-radius:50%;background:var(--footer-text)}
  .footer-rule{position:absolute;left:240px;top:248px;width:720px;height:1px;background:#3a4550}
  .social{position:absolute;left:262px;top:266px;display:flex;gap:10px}
  .social span{width:13px;height:13px;border-radius:50%;background:var(--footer-text)}
  .copyright{position:absolute;left:0;width:1200px;top:266px;text-align:center;font-size:11px}
  .payments{position:absolute;left:740px;top:263px;display:flex;gap:6px}
  .payments span{width:28px;height:18px;border-radius:3px;background:#d8dde0}
</style>
</head>
<body>

<header class="site-header">
  <div class="brand">VESTERLUND</div>
  <nav class="main-nav">
    <a class="is-active" href="#">Home</a>
    <a href="#">About Us</a>
    <a href="#">Contact Us</a>
    <a href="#">Order Tracking</a>
  </nav>
</header>

<section class="hero">
  <div class="hero-photo" role="img" aria-label="Woman with a towel on her hair applying serum to her cheek"></div>
  <div class="hero-bottle" role="img" aria-label="Teal serum dropper bottle"></div>
  <h1 class="hero-title"><span class="line-1">Your Daily</span><span class="line-2">Skin Insurance</span></h1>
  <a class="btn" href="#">Shop Now</a>
  <div class="slider-dots"><span></span><span></span><span></span></div>
  <svg class="hero-wave" viewBox="0 0 1200 180" preserveAspectRatio="none">
    <path d="M0 60 Q600 230 1200 20 L1200 180 L0 180 Z" fill="#ffffff"/>
    <path d="M0 60 Q600 230 1200 20" fill="none" stroke="#2f7f86" stroke-width="4"/>
  </svg>
</section>

<!-- Feature 1 -->
<div class="feature-photo" style="left:248px;top:712px;background:linear-gradient(135deg,#2d5a78,#6b8fb0 60%,#c9a894)" role="img" aria-label="Woman looking at a glowing phone screen at night"></div>
<div class="feature-text" style="left:620px;top:775px">
  <div class="kicker">Protect Your Face</div>
  <div class="headline">From Daily Free Radicals</div>
  <p>Daily exposure to sun, smoke and city air creates free radicals that quietly break down collagen and weaken the skin barrier. Our serum forms a light protective layer that helps neutralise this stress before it leaves a mark, so your skin stays firm, calm and even through every busy day of the week.</p>
</div>

<!-- Feature 2 -->
<div class="feature-text" style="left:230px;top:1060px">
  <div class="kicker">Block Wrinkles</div>
  <div class="headline">Before They Occur</div>
  <p>Fine lines form slowly, long before we see them in the mirror. With daily care you can support natural renewal and keep moisture locked in where it matters most. Start early, stay consistent, and let your skin show the results of steady protection instead of late repair.</p>
</div>
<div class="feature-photo" style="left:650px;top:1100px;background:linear-gradient(135deg,#e6cbb8,#d3ab93 60%,#b88c78)" role="img" aria-label="Close-up of a mature woman's eye area and skin"></div>

<!-- Feature 3 -->
<div class="feature-photo" style="left:248px;top:1480px;background:linear-gradient(135deg,#f1e4da,#e0c7b5 60%,#cfae9a)" role="img" aria-label="Woman touching her face with both hands"></div>
<div class="feature-text" style="left:620px;top:1545px">
  <div class="kicker">Boost Your Daily</div>
  <div class="headline">Cell Renewal</div>
  <p>As we age, cell turnover slows and skin can look dull and tired. Our blend of gentle actives encourages fresh cells to rise to the surface, restoring a smooth texture and a healthy glow. A few drops each morning are all it takes to wake up your complexion.</p>
</div>

<!-- Guarantee -->
<svg class="guarantee" viewBox="0 0 1200 840" preserveAspectRatio="none">
  <defs>
    <linearGradient id="bandFill" x1="0" y1="0" x2="0" y2="1">
      <stop offset="0" stop-color="#2c6e73"/>
      <stop offset="0.5" stop-color="#1f5a60"/>
      <stop offset="1" stop-color="#2f767b"/>
    </linearGradient>
  </defs>
  <path d="M0 40 Q600 200 1200 40 L1200 620 Q600 1004 0 620 Z" fill="url(#bandFill)"/>
  <path d="M0 40 Q600 200 1200 40" fill="none" stroke="#5fa9ad" stroke-width="6"/>
  <path d="M0 620 Q600 1004 1200 620" fill="none" stroke="#5fa9ad" stroke-width="6"/>
</svg>
<h2 class="guarantee-title">Your Security Guarantee</h2>
<p class="guarantee-copy">Every bottle is made in a certified clean laboratory under strict quality control. We test each batch for purity and stability, and if you are not fully satisfied within thirty days, we will refund your order without questions.</p>
<div class="guarantee-video" role="img" aria-label="Video still of a laboratory technician in a mask and cap at work"></div>
<svg class="play-button" viewBox="0 0 44 44">
  <circle cx="22" cy="22" r="21" fill="rgba(255,255,255,.85)"/>
  <path d="M18 14 L31 22 L18 30 Z" fill="#1f5a60"/>
</svg>

<!-- Brand promise -->
<section class="promise">
  <div class="promise-brand">VESTERLUND</div>
  <h2 class="promise-title">Protect Your Most Beautiful Property</h2>
  <p class="promise-copy">With the perfect balance of active ingredients and lightweight texture, our serum gives your skin the care it deserves, keeping it protected and radiant every day.</p>
  <div class="promise-initial" role="img" aria-label="Faint large monogram background"></div>
  <div class="promise-bottle" role="img" aria-label="Teal facial day repair serum bottle with dropper"></div>
  <a class="btn" href="#">Learn More</a>
</section>

<footer class="site-footer">
  <div class="brand">VESTERLUND</div>
  <div class="footer-cols">
    <ul style="left:262px"><li>Home</li><li>About Us</li><li>Cooperation</li><li>Fabrication</li></ul>
    <ul style="left:525px"><li>Customer Service</li><li>Contact Us</li><li>Order Tracking</li></ul>
    <ul style="left:800px"><li>New Order</li><li>Delivery</li><li>Privacy Policy</li></ul>
  </div>
  <div class="footer-rule"></div>
  <div class="social"><span></span><span></span><span></span><span></span><span></span></div>
  <div class="copyright">Copyright © 2024 Vesterlund | All Rights Reserved</div>
  <div class="payments"><span></span><span></span><span></span><span></span><span></span><span></span></div>
</footer>

</body>
</html>
```